Website For Custom Home Builder

-Very elegant and simple design as I am a high end custom home builder.
-I build homes $2 million to $10 million range so the website needs to reflect the level of home that I build.
-Attached are photos of homes I have built to use as well as my logo.
-I need final design to be in layered format so my local guy can edit if he needs to.

3 Page Design
1. HomePage:
-logo, some photos,
-“Building beautiful custom homes in Indianapolis for over 20 years”
2. AboutPage:
-Dean Morley has been building stunning custom homes in the Indianpolis area for over 20 years. As a small boutique building company we only build a handful of homes a year in order to offer our clients the personal attention that their homes deserve. It's this attention to detail that makes our client experience and final product something special and unique.
- family photo
3. ContactPage:
-office photo
-317-555-0192
-dean@dmbuildco.example
-415 North Larkwood Dr, Suite 310, Carmel IN 46099

Target Market(s)

Very high end clients looking to build $2 million to $10 million homes.

Industry/Entity Type

Residential high end custom home builder/construction

Coding

Coded - Design and coding required

Number of Pages Required

3 page

Requirements
Must have
• Very simple and elegant design that represents the high end homes that I build.
Nice to have
Should not have
• Should NOT have a lot of clutter or be a very busy page from a design perspective.

```html
<!DOCTYPE html>
<html lang="en">
<head>
<meta charset="utf-8">
<title>About Us – Dean Morley Custom Homes</title>
<link href="https://fonts.googleapis.com/css2?family=Montserrat:wght@600;700&family=Questrial&display=swap" rel="stylesheet">
<style>
:root{
  --rust:#a6561a;
  --ink:#1e1e1e;
  --text:#3a3a3a;
  --white:#ffffff;
  --mist:#f7f7f7;
  --line:#cfcfcf;
}
*{box-sizing:border-box;margin:0;padding:0}
html,body{width:928px;height:1200px;overflow:hidden;background:var(--white)}
body{position:relative;font-family:"Questrial",sans-serif;color:var(--text)}
.abs{position:absolute}

/* header */
.site-header{left:0;top:0;width:928px;height:81px;background:var(--white)}
.brand{left:93px;top:26px;display:flex;align-items:center;gap:7px}
.brand-mark{width:12px;height:12px;background:var(--rust)}
.brand-name{font-family:"Questrial",sans-serif;font-size:17px;color:var(--ink);letter-spacing:.5px}
.main-nav a{position:absolute;top:33px;font-size:9.5px;letter-spacing:.4px;color:var(--ink);text-decoration:none}
.main-nav a.is-active{color:var(--rust)}
.call-box{left:662px;top:0;width:266px;height:81px;background:var(--rust);color:var(--white);padding:20px 0 0 23px}
.call-label{font-size:14px;letter-spacing:.8px;display:flex;align-items:center;gap:9px}
.call-number{font-family:"Montserrat",sans-serif;font-weight:700;font-size:20px;letter-spacing:.6px;margin-top:4px}

/* hero */
.page-hero{left:0;top:81px;width:928px;height:232px;background:linear-gradient(180deg,#5b5246 0%,#3c352c 45%,#2d2820 100%)}
.hero-glow{left:380px;top:190px;width:360px;height:110px;background:radial-gradient(ellipse at center,rgba(214,150,55,.45),rgba(214,150,55,0) 70%)}
.hero-title{left:0;top:172px;width:928px;text-align:center;font-family:"Montserrat",sans-serif;font-weight:700;font-size:30px;color:var(--white)}
.hero-rule{top:213px;height:1.5px;background:var(--white)}

/* about */
.about-accent{left:93px;top:370px;width:303px;height:343px;background:var(--rust)}
.about-photo{left:116px;top:393px;width:303px;height:344px;background:linear-gradient(180deg,#d9d9db 0%,#cfcfcf 45%,#b7a58e 75%,#c8b59a 100%)}
.about-kicker{left:473px;top:503px;font-size:15px;color:var(--rust);letter-spacing:.4px}
.about-title{left:473px;top:522px;font-family:"Montserrat",sans-serif;font-weight:700;font-size:30px;color:var(--ink)}
.about-copy{left:473px;top:573px;width:358px;font-size:9.9px;line-height:16.2px;color:var(--text)}

/* contact */
.contact-section{left:0;top:795px;width:928px;height:371px;background:var(--mist)}
.contact-kicker{left:0;top:849px;width:928px;text-align:center;font-size:15px;color:var(--rust)}
.contact-title{left:0;top:868px;width:928px;text-align:center;font-family:"Montserrat",sans-serif;font-weight:700;font-size:30px;color:var(--ink)}
.field{border:1px solid var(--line);background:transparent;border-radius:2px;font-size:9px;color:#555;padding:9px 10px;letter-spacing:.3px}
.submit-btn{left:418px;top:1079px;width:92px;height:29px;border:1px solid var(--rust);color:var(--rust);font-size:9px;letter-spacing:.6px;display:flex;align-items:center;justify-content:center;border-radius:2px}

/* footer */
.site-footer{left:0;top:1166px;width:928px;height:34px;background:var(--rust);color:var(--white);font-size:8px}
.site-footer span{position:absolute;top:13px}
.site-footer b{font-weight:700}
.site-footer u{text-decoration:underline}
</style>
</head>
<body>

<header class="abs site-header">
  <div class="abs brand"><span class="brand-mark"></span><span class="brand-name">DEAN MORLEY</span></div>
  <nav class="main-nav">
    <a href="#" style="left:390px">HOME</a>
    <a href="#" class="is-active" style="left:463px">ABOUT US</a>
    <a href="#" style="left:555px">CONTACT US</a>
  </nav>
  <div class="abs call-box">
    <div class="call-label">CALL US
      <svg width="14" height="14" viewBox="0 0 24 24" fill="none" stroke="#fff" stroke-width="2.2" stroke-linecap="round" stroke-linejoin="round"><path d="M22 16.9v3a2 2 0 0 1-2.2 2 19.8 19.8 0 0 1-8.6-3.1 19.5 19.5 0 0 1-6-6A19.8 19.8 0 0 1 2.1 4.2 2 2 0 0 1 4.1 2h3a2 2 0 0 1 2 1.7c.1.9.4 1.8.7 2.7a2 2 0 0 1-.5 2.1L8 9.8a16 16 0 0 0 6 6l1.3-1.3a2 2 0 0 1 2.1-.4c.9.3 1.8.6 2.7.7a2 2 0 0 1 1.7 2z"/></svg>
    </div>
    <div class="call-number">317-555-0192</div>
  </div>
</header>

<section class="abs page-hero" role="img" aria-label="Dusk photograph of a large stone and timber custom home with warmly lit windows"></section>
<div class="abs hero-glow"></div>
<h1 class="abs hero-title">ABOUT US</h1>
<div class="abs hero-rule" style="left:422px;width:34px"></div>
<div class="abs hero-rule" style="left:462px;width:4px"></div>
<div class="abs hero-rule" style="left:472px;width:34px"></div>

<div class="abs about-accent"></div>
<div class="abs about-photo" role="img" aria-label="Family photograph of parents and a child sitting on a rug in a bright living room"></div>
<p class="abs about-kicker">ABOUT THE</p>
<h2 class="abs about-title">DEAN MORLEY</h2>
<p class="abs about-copy">Dean Morley has been building stunning custom homes in the Indianpolis area for over 20 years. As a small boutique building company we only build a handful of homes a year in order to offer our clients the personal attention that their homes deserve. It's this attention to detail that makes our client experience and final product something special and unique.</p>

<section class="abs contact-section"></section>
<p class="abs contact-kicker">ENQUIRY NOW!</p>
<h2 class="abs contact-title">CONTACT US</h2>
<div class="abs field" style="left:180px;top:923px;width:275px;height:29px">Full Name</div>
<div class="abs field" style="left:473px;top:923px;width:275px;height:29px">Email Address*</div>
<div class="abs field" style="left:180px;top:963px;width:275px;height:29px">Phone Number*</div>
<div class="abs field" style="left:473px;top:963px;width:275px;height:29px">Subject</div>
<div class="abs field" style="left:180px;top:1004px;width:568px;height:57px">Messages...</div>
<div class="abs submit-btn">SUBMIT</div>

<footer class="abs site-footer">
  <span style="left:92px"><b>E.:</b> <u>dean@dmbuildco.example</u></span>
  <span style="left:336px"><b>ADDRESS:</b> 415 North Larkwood Dr, Suite 310, Carmel IN 46099</span>
  <span style="left:654px">© Copyright <u>Dean Morley.</u> All Right Reserved.</span>
</footer>

</body>
</html>
```